Business Createrer

Design an info-graphic which explains the process of what I do to help people and busnesses (Hotels, venues etc) divine a food and Beverage plan for success.

I have an existing website which shows the style I would like to use visit www.benjarvisfield.com.au.

I have attached a PPTX showing the 4 components required and then a second page for the process and a copy of the logo and splash images.

I this works I have further design projects including promo videos for apps

Target Market(s)

Food and Beverage industry including hotels, venues, caterers and restaurants

Industry/Entity Type

Business Consultant

Other font styles liked:
• sweet sans

Requirements
Must have
• icon creations and clear workflow

```html
<!DOCTYPE html>
<html lang="en">
<head>
<meta charset="utf-8">
<title>Dining Concept Process – Ben Jarvisfield</title>
<link rel="stylesheet" href="https://fonts.googleapis.com/css2?family=Montserrat:wght@400;600;700&family=Arimo:wght@400&display=swap">
<style>
  :root {
    --sky: #acd5e6;
    --lagoon: #7fbfdf;
    --ocean: #3b8fc6;
    --navy: #3563a0;
    --mist: #c9e3ef;
    --plate: #b3d9ea;
    --badge: #aed6e8;
    --ink: #4a5663;
    --white: #ffffff;
  }
  html, body { margin: 0; padding: 0; width: 1200px; height: 772px; overflow: hidden; background: var(--sky); }
  .infographic { display: block; width: 1200px; height: 772px; }
  .title { font-family: "Montserrat", sans-serif; font-weight: 700; fill: var(--ink); font-size: 14px; letter-spacing: .3px; }
  .title-light { font-family: "Montserrat", sans-serif; font-weight: 400; fill: var(--ink); font-size: 13px; }
  .label { font-family: "Montserrat", sans-serif; font-weight: 700; fill: var(--ink); font-size: 12px; letter-spacing: .3px; }
  .body { font-family: "Arimo", sans-serif; fill: var(--ink); font-size: 12px; }
  .step-word { font-family: "Montserrat", sans-serif; font-weight: 700; fill: var(--navy); font-size: 10px; }
  .step-num { font-family: "Montserrat", sans-serif; font-weight: 700; fill: var(--navy); font-size: 28px; }
  .flow { fill: none; stroke: var(--white); stroke-width: 2; }
  .icon { fill: var(--navy); }
  .brand-name { font-family: "Montserrat", sans-serif; font-weight: 400; fill: var(--ocean); font-size: 38px; }
</style>
</head>
<body>
<svg class="infographic" viewBox="0 0 1400 901" xmlns="http://www.w3.org/2000/svg">
  <defs>
    <g id="step-badge">
      <circle r="30" fill="var(--badge)" stroke="var(--white)" stroke-width="3"/>
    </g>
    <path id="arrow-left" d="M0 0 L12 -7 V7 Z" fill="var(--white)"/>
    <path id="arrow-right" d="M0 0 L-12 -7 V7 Z" fill="var(--white)"/>
    <radialGradient id="plate-fill">
      <stop offset="0" stop-color="#3563a0"/>
      <stop offset=".62" stop-color="#3a6aa6"/>
      <stop offset="1" stop-color="#b3d9ea"/>
    </radialGradient>
  </defs>

  <!-- backgrounds -->
  <rect class="band-top" x="0" y="0" width="1400" height="500" fill="var(--sky)"/>
  <rect class="band-middle" x="0" y="500" width="1400" height="330" fill="var(--lagoon)"/>
  <rect class="band-bottom" x="0" y="830" width="1400" height="71" fill="var(--ocean)"/>

  <!-- components tag -->
  <g class="components-tag">
    <rect x="188" y="0" width="162" height="218" fill="var(--mist)"/>
    <path d="M188 198 H210 V218 Z" fill="var(--ocean)"/>
    <text class="title" x="213" y="135">FOUR</text>
    <text class="title" x="213" y="153">COMPONENTS</text>
    <text class="title-light" x="213" y="171">THAT MAKE UP A</text>
    <text class="title-light" x="213" y="188">DINING CONCEPT</text>
    <line x1="365" y1="110" x2="365" y2="200" stroke="var(--white)" stroke-width="1.5"/>
  </g>

  <!-- component icons -->
  <g class="component beverage">
    <path class="icon" d="M389 127 H411 L400 140 V156 H406 V159 H394 V156 H400 V140 Z"/>
    <circle cx="396" cy="130" r="5" fill="var(--ocean)"/>
    <path class="icon" d="M421 103 H428 V115 Q435 122 435 130 V158 H414 V130 Q414 122 421 115 Z"/>
    <path class="icon" d="M437 128 H453 Q453 142 446 145 V156 H451 V159 H441 V156 H444 V145 Q437 142 437 128 Z"/>
    <text class="label" x="425" y="183" text-anchor="middle">BEVERAGE</text>
  </g>
  <g class="component food">
    <circle class="icon" cx="556" cy="130" r="3"/>
    <path class="icon" d="M528 158 Q528 132 556 132 Q584 132 584 158 Z"/>
    <rect class="icon" x="524" y="158" width="64" height="4" rx="2"/>
    <text class="label" x="555" y="183" text-anchor="middle">FOOD</text>
  </g>
  <g class="component brand">
    <path class="icon" d="M657 108 V124 Q657 130 661 131 V158 H664 V131 Q668 130 668 124 V108 H666 V122 H664 V108 H662 V122 H660 V108 Z"/>
    <circle class="icon" cx="694" cy="133" r="25"/>
    <circle cx="694" cy="133" r="17" fill="none" stroke="var(--sky)" stroke-width="2"/>
    <path class="icon" d="M723 108 Q729 120 727 136 H725 V158 H721 V108 Z"/>
    <text class="label" x="695" y="183" text-anchor="middle">BRAND</text>
  </g>
  <g class="component environment" fill="none" stroke="var(--navy)" stroke-width="4">
    <path d="M788 100 V158 M788 136 H812 V158 M788 143 H812"/>
    <path d="M872 100 V158 M872 136 H848 V158 M872 143 H848"/>
    <path d="M806 120 H854 M830 120 V158 M822 158 H838"/>
    <path d="M815 106 H821 L818 112 V118 M842 106 H848 L845 112 V118 M830 103 V118" stroke-width="2.5"/>
    <text class="label" x="830" y="183" text-anchor="middle" stroke="none" fill="var(--ink)">ENVIRONMENT</text>
  </g>

  <!-- bracket & underlines -->
  <g class="connectors">
    <path class="flow" d="M380 193 H475 M502 193 H612 M637 193 H747 M772 193 H882"/>
    <path class="flow" d="M422 193 V208 Q422 220 434 220 H816 Q828 220 828 208 V193 M555 193 V220 M692 193 V220"/>
    <path class="flow" d="M620 220 V300 L576 333"/>
  </g>

  <!-- main flow -->
  <path class="flow" d="M576 333 H248 C285 370 275 430 228 453 H520 C545 490 530 555 572 574 H300 Q275 574 275 600 V775 Q275 790 290 790 H388 Q400 790 400 778 V695 H745 Q747 695 747 707 V778 Q747 790 759 790 H1206 Q1218 790 1218 778 V645 H1122 Q1112 645 1112 635 V522 Q1112 512 1122 512 H1208 Q1218 512 1218 502 V453 H895"/>
  <use href="#arrow-left" x="338" y="333"/>
  <use href="#arrow-right" x="500" y="453"/>
  <use href="#arrow-left" x="358" y="574"/>
  <path d="M275 682 L268 670 H282 Z" fill="var(--white)"/>
  <use href="#arrow-right" x="344" y="790"/>
  <use href="#arrow-right" x="477" y="695"/>
  <use href="#arrow-right" x="706" y="695"/>
  <path d="M1218 704 L1211 716 H1225 Z" fill="var(--white)"/>
  <path d="M1112 572 L1105 584 H1119 Z" fill="var(--white)"/>
  <use href="#arrow-left" x="1100" y="453"/>
  <path d="M866 453 L894 437 V469 Z" fill="var(--white)"/>

  <!-- magnifier illustration area -->
  <g class="magnifier-art" role="img" aria-label="Illustration: magnifying glass over a plate with a dining table, fork and knife">
    <circle cx="160" cy="398" r="80" fill="url(#plate-fill)"/>
  </g>

  <!-- central plate illustration area -->
  <g class="plate-art" role="img" aria-label="Illustration: fork and knife beside a plate showing a dining table with chairs and a cloche">
    <circle cx="697" cy="455" r="152" fill="url(#plate-fill)" stroke="var(--white)" stroke-width="2"/>
  </g>

  <!-- step badges -->
  <g class="step step-1" transform="translate(465 333)"><use href="#step-badge"/><text class="step-word" y="-8" text-anchor="middle">STEP</text><text class="step-num" y="18" text-anchor="middle">1</text></g>
  <g class="step step-2" transform="translate(302 453)"><use href="#step-badge"/><text class="step-word" y="-8" text-anchor="middle">STEP</text><text class="step-num" y="18" text-anchor="middle">2</text></g>
  <g class="step step-3" transform="translate(465 574)"><use href="#step-badge"/><text class="step-word" y="-8" text-anchor="middle">STEP</text><text class="step-num" y="18" text-anchor="middle">3</text></g>
  <g class="step step-4" transform="translate(578 693)"><use href="#step-badge"/><text class="step-word" y="-8" text-anchor="middle">STEP</text><text class="step-num" y="18" text-anchor="middle">4</text></g>
  <g class="step step-5" transform="translate(1217 453)"><use href="#step-badge"/><text class="step-word" y="-8" text-anchor="middle">STEP</text><text class="step-num" y="18" text-anchor="middle">5</text></g>
  <g class="step step-6" transform="translate(947 453)"><use href="#step-badge"/><text class="step-word" y="-8" text-anchor="middle">STEP</text><text class="step-num" y="18" text-anchor="middle">6</text></g>

  <!-- step captions -->
  <g class="caption">
    <text class="title" x="431" y="358" text-anchor="end">COMPARE</text>
    <text class="body" x="431" y="375" text-anchor="end">the proposed</text>
    <text class="body" x="431" y="389" text-anchor="end">new concept to</text>
    <text class="body" x="431" y="402" text-anchor="end">market</text>
  </g>
  <g class="caption">
    <text class="title" x="339" y="479">ITERATIVELY REFINE</text>
    <text class="body" x="339" y="495">the new concept</text>
  </g>
  <g class="caption">
    <text class="title" x="431" y="599" text-anchor="end">CREATE A</text>
    <text class="title" x="431" y="617" text-anchor="end">BUSINESS MODEL</text>
    <text class="body" x="431" y="637" text-anchor="end">for the new concept</text>
  </g>
  <g class="caption">
    <text class="title" x="614" y="723">DETAILING</text>
    <text class="body" x="614" y="742">to make the</text>
    <text class="body" x="614" y="754">business model</text>
    <text class="body" x="614" y="766">work</text>
  </g>
  <g class="caption speech">
    <path d="M953 287 H1128 Q1138 287 1138 297 V375 Q1138 385 1128 385 H1000 L963 415 L975 385 H953 Q943 385 943 375 V297 Q943 287 953 287 Z" fill="var(--mist)"/>
    <text class="title" x="972" y="324">SET UP &amp; DELIVER</text>
    <text class="body" x="972" y="343">the new dining concept</text>
    <text class="body" x="972" y="356">consistently and elegantly</text>
  </g>

  <!-- presentation board -->
  <g class="board">
    <rect x="296" y="680" width="86" height="4" fill="var(--navy)"/>
    <rect x="300" y="684" width="78" height="58" fill="none" stroke="var(--navy)" stroke-width="3"/>
    <rect x="296" y="742" width="86" height="4" fill="var(--navy)"/>
    <path d="M339 746 V770 M339 752 L318 770 M339 752 L360 770" stroke="var(--navy)" stroke-width="3"/>
    <rect class="icon" x="329" y="696" width="20" height="12"/>
    <path d="M339 708 V716 M315 716 H363 M315 716 V722 M339 716 V722 M363 716 V722" stroke="var(--navy)" stroke-width="2" fill="none"/>
    <rect class="icon" x="306" y="722" width="18" height="11"/>
    <rect class="icon" x="330" y="722" width="18" height="11"/>
    <rect class="icon" x="354" y="722" width="18" height="11"/>
  </g>

  <!-- detailing icons -->
  <g class="detail procedures">
    <path class="icon" d="M781 684 H815 V718 L805 728 H781 Z"/>
    <path d="M787 694 H809 M787 700 H809 M787 706 H809 M787 712 H809 M787 718 H803" stroke="var(--white)" stroke-width="1.5"/>
    <text class="body" x="801" y="756" text-anchor="middle">• Operational</text>
    <text class="body" x="801" y="768" text-anchor="middle">Procedures</text>
  </g>
  <g class="detail sourcing">
    <rect class="icon" x="848" y="678" width="42" height="34" rx="4"/>
    <rect x="852" y="682" width="34" height="24" fill="var(--white)" rx="2"/>
    <path class="icon" d="M892 690 H904 L914 704 V718 H892 Z"/>
    <rect class="icon" x="848" y="712" width="66" height="6"/>
    <circle class="icon" cx="870" cy="722" r="8"/><circle class="icon" cx="898" cy="722" r="8"/>
    <circle cx="870" cy="722" r="3" fill="var(--lagoon)"/><circle cx="898" cy="722" r="3" fill="var(--lagoon)"/>
    <text class="body" x="880" y="756" text-anchor="middle">• Sourcing</text>
  </g>
  <g class="detail staffing">
    <circle class="icon" cx="973" cy="688" r="5"/><path class="icon" d="M965 703 Q965 694 973 694 Q981 694 981 703 Z"/>
    <path d="M973 704 V710 M958 710 H988 M958 710 V714 M988 710 V714" stroke="var(--navy)" stroke-width="2" fill="none"/>
    <circle class="icon" cx="958" cy="716" r="5"/><path class="icon" d="M950 730 Q950 722 958 722 Q966 722 966 730 Z"/>
    <circle class="icon" cx="988" cy="716" r="5"/><path class="icon" d="M980 730 Q980 722 988 722 Q996 722 996 730 Z"/>
    <text class="body" x="976" y="756" text-anchor="middle">• Staffing Models</text>
    <text class="body" x="980" y="768" text-anchor="middle">with roles and</text>
    <text class="body" x="972" y="780" text-anchor="middle">hierarchies</text>
  </g>
  <g class="detail marketing">
    <rect class="icon" x="1049" y="708" width="12" height="18"/>
    <rect class="icon" x="1064" y="700" width="12" height="26"/>
    <rect class="icon" x="1079" y="694" width="12" height="32"/>
    <rect class="icon" x="1043" y="727" width="54" height="3"/>
    <path d="M1047 700 L1062 690 L1072 694 L1088 684" stroke="var(--navy)" stroke-width="2" fill="none"/>
    <path class="icon" d="M1092 681 L1083 682 L1089 689 Z"/>
    <text class="body" x="1072" y="756" text-anchor="middle">• Sales and</text>
    <text class="body" x="1073" y="768" text-anchor="middle">Marketing</text>
    <text class="body" x="1062" y="780" text-anchor="middle">Plans</text>
  </g>
  <g class="detail financial">
    <rect class="icon" x="1127" y="698" width="48" height="24" rx="3"/>
    <rect x="1131" y="692" width="52" height="26" rx="3" fill="var(--navy)" stroke="var(--lagoon)" stroke-width="2"/>
    <text x="1157" y="711" text-anchor="middle" font-family="Montserrat, sans-serif" font-weight="700" font-size="16" fill="var(--white)">$</text>
    <text class="body" x="1158" y="756" text-anchor="middle">• Financial</text>
    <text class="body" x="1159" y="768" text-anchor="middle">models</text>
  </g>

  <!-- blueprint icons -->
  <g class="blueprints">
    <path class="icon" d="M1134 530 H1162 V576 H1126 V538 Z"/>
    <path d="M1132 552 Q1132 540 1144 540 Q1156 540 1156 552 Z M1130 554 H1158 M1132 560 H1156 M1132 565 H1156 M1132 570 H1156" stroke="var(--white)" stroke-width="2" fill="none"/>
    <path class="icon" d="M1178 530 H1206 V576 H1170 V538 Z"/>
    <path d="M1176 542 H1186 L1181 548 V554 M1190 536 V554 M1194 544 H1202 Q1202 552 1198 552 V554 M1176 560 H1200 M1176 565 H1200 M1176 570 H1200" stroke="var(--white)" stroke-width="2" fill="none"/>
    <path class="icon" d="M1134 584 H1162 V630 H1126 V592 Z"/>
    <path d="M1132 596 H1150 V624 H1132 Z M1141 600 V608 M1137 604 H1145" stroke="var(--white)" stroke-width="2" fill="none"/>
    <circle cx="1141" cy="616" r="3" fill="var(--white)"/>
    <path class="icon" d="M1178 584 H1206 V630 H1170 V592 Z"/>
    <circle cx="1189" cy="608" r="10" fill="var(--white)"/>
    <circle cx="1189" cy="608" r="6" fill="var(--navy)"/>
    <path d="M1175 598 V620 M1202 598 V620" stroke="var(--white)" stroke-width="2"/>
    <text class="title" x="1222" y="540">CREATE BLUEPRINTS</text>
    <text class="title" x="1222" y="560">FOR EXECUTION</text>
    <text class="body" x="1222" y="578">• Menus</text>
    <text class="body" x="1222" y="595">• Drinks</text>
    <text class="body" x="1222" y="611">• Floor Plans</text>
    <text class="body" x="1222" y="627">• Brand Concept</text>
  </g>

  <!-- brand name corner -->
  <g class="brand-corner">
    <rect x="1330" y="830" width="70" height="71" fill="var(--white)"/>
    <text class="brand-name" x="1335" y="870">BJ</text>
  </g>
</svg>
</body>
</html>
```